Business card design, sleek & clean . For a notary loan signing business. I work with several lenders escrow officers etc . I am bilingual in Spanish , work 7 days a week to meet clients needs. Loan documents can be emailed for printing.

Logo Text

Not sure sleek clean logo

```html
<!DOCTYPE html>
<html lang="en">
<head>
<meta charset="utf-8">
<title>Marisol Orozco – Certified Signing Agent</title>
<link rel="stylesheet" href="https://fonts.googleapis.com/css2?family=Open+Sans:wght@400&family=Montserrat:wght@500;600&family=Libre+Baskerville:wght@400&display=swap">
<style>
  :root {
    --page: #f2f2f4;
    --card: #ffffff;
    --navy: #1f2150;
    --gold: #e3bf6a;
    --gold-soft: #ebcf8b;
  }
  * { margin: 0; padding: 0; box-sizing: border-box; }
  html, body {
    width: 1200px;
    height: 962px;
    overflow: hidden;
    background: var(--page);
  }
  .card {
    position: absolute;
    left: 60px;
    top: 162px;
    width: 1080px;
    height: 637px;
    background: var(--card);
  }
  .contact-list {
    position: absolute;
    left: 96px;
    top: 0;
    list-style: none;
    font-family: "Open Sans", Arial, sans-serif;
    font-size: 28px;
    color: var(--navy);
  }
  .contact-item {
    position: absolute;
    left: 0;
    display: flex;
    align-items: center;
    white-space: nowrap;
    transform: translateY(-50%);
  }
  .contact-item .marker {
    width: 31px;
    height: 31px;
    margin-right: 16px;
    flex: none;
    display: flex;
    align-items: center;
    justify-content: center;
  }
  .marker .dot {
    width: 11px;
    height: 11px;
    border-radius: 50%;
    background: var(--gold);
  }
  .item-phone { top: 264px; }
  .item-email { top: 313px; }
  .item-spanish { top: 366px; }
  .item-printing { top: 413px; }

  .divider {
    position: absolute;
    left: 541px;
    top: 109px;
    width: 3px;
    height: 419px;
    background: linear-gradient(to bottom, rgba(227,191,106,0) 0%, var(--gold) 20%, var(--gold) 80%, rgba(227,191,106,0) 100%);
    border-radius: 2px;
  }
  .brand {
    position: absolute;
    left: 626px;
    top: 290px;
    width: 358px;
    text-align: center;
  }
  .brand-name {
    font-family: "Libre Baskerville", Georgia, serif;
    font-size: 29px;
    font-weight: 400;
    color: var(--gold);
    letter-spacing: 0.5px;
    white-space: nowrap;
  }
  .brand-title {
    margin-top: 6px;
    font-family: "Montserrat", Arial, sans-serif;
    font-weight: 500;
    font-size: 19px;
    letter-spacing: 4.6px;
    color: var(--navy);
    white-space: nowrap;
  }
  .availability {
    position: absolute;
    left: 0;
    width: 1080px;
    top: 564px;
    text-align: center;
    font-family: "Montserrat", Arial, sans-serif;
    font-weight: 600;
    font-size: 17px;
    color: var(--navy);
    letter-spacing: 0.3px;
  }
  .message-badge {
    position: absolute;
    left: 947px;
    top: 555px;
    width: 32px;
    height: 32px;
    border-radius: 50%;
    background: var(--navy);
  }
</style>
</head>
<body>
  <main class="card">
    <ul class="contact-list">
      <li class="contact-item item-phone">
        <span class="marker">
          <svg width="31" height="31" viewBox="0 0 31 31" aria-hidden="true">
            <rect width="31" height="31" rx="5" fill="var(--gold)"/>
            <path d="M11 7 C8 8 8 11 9 15 C10 19 13 23 17 24 C19 25 21 24 22 22 L19 19 L17 20 C15 19 13 16 13 13 L15 12 Z" fill="#fff"/>
          </svg>
        </span>
        <span class="contact-text">(555)014-2273</span>
      </li>
      <li class="contact-item item-email">
        <span class="marker">
          <svg width="31" height="31" viewBox="0 0 31 31" aria-hidden="true">
            <rect width="31" height="31" rx="5" fill="var(--gold)"/>
            <rect x="6" y="9" width="19" height="13" fill="none" stroke="#fff" stroke-width="2"/>
            <path d="M6 9 L15.5 17 L25 9" fill="none" stroke="#fff" stroke-width="2"/>
          </svg>
        </span>
        <span class="contact-text">morozco_signs@example.com</span>
      </li>
      <li class="contact-item item-spanish">
        <span class="marker"><span class="dot"></span></span>
        <span class="contact-text">Hablo Espanol</span>
      </li>
      <li class="contact-item item-printing">
        <span class="marker"><span class="dot"></span></span>
        <span class="contact-text">Loan packaging &amp; printing</span>
      </li>
    </ul>

    <div class="divider"></div>

    <div class="brand">
      <p class="brand-name">MARISOL OROZCO</p>
      <p class="brand-title">CERTIFIED SIGNING AGENT</p>
    </div>

    <p class="availability">7 DAYS A WEEK TO MEET YOUR CLIENTS NEEDS</p>
    <span class="message-badge" role="img" aria-label="Messaging app contact"></span>
  </main>
</body>
</html>
```